Business Card and Stationary Design

After the successful redesign of our logo we are wanting to follow suite and create a new business card and stationary design!

New Logo is attached, information required on the business card should contain a mixture of the following but layout/arrangement is up to the designer.

Happy if the national provider number and abn are on the back, and happy for them to be smaller than the rest.

I am also happy to receive single sided or weird and wonderful designs.

Name
Title
National Provider Number 7192
ABN 53 614 289 117
Level 1, 214 Garrow Street
Hexham NSW 2322
Ph: 1300 587 902
Mobile: 0438 761 205
name@ironquillbuild.com.au
www.ironquillbuild.com.au

Target Market(s)

Professionals, Peers, Students, Suppliers...

Industry/Entity Type

Construction

Contact Information for Business Card

Listed in project description

Font styles to use
Other font styles liked:
• Century Gothic

Colors
0455a3
3176b5
ffffff

Requirements
Must have
• Professional Design, same color scheme as our logo
Nice to have
• Something that sets our apart from everyone else would be fantastic, open to size and shape and layout options, as long as they present professionally.
• Open to raised/embossed text, alternative materials, custom sizes, clear material
Should not have
• The color orange

```html
<!DOCTYPE html>
<html lang="en">
<head>
<meta charset="utf-8">
<title>Ironquill Build – Business Card</title>
<link rel="stylesheet" href="https://fonts.googleapis.com/css2?family=Questrial&family=Montserrat:wght@600;700&display=swap">
<style>
  :root {
    --navy: #1f3a80;
    --navy-light: #2d4d93;
    --grey: #808080;
    --text-grey: #6b6b6b;
    --white: #ffffff;
    --backdrop: #e9e9eb;
  }
  * { box-sizing: border-box; margin: 0; padding: 0; }
  html, body { width: 1200px; height: 1000px; overflow: hidden; }
  body { background: var(--backdrop); position: relative; font-family: "Questrial", sans-serif; }

  .card { position: absolute; left: 269px; width: 662px; height: 379px; box-shadow: 0 3px 8px rgba(0,0,0,.25); overflow: hidden; }

  /* Front */
  .card-front { top: 108px; background: linear-gradient(120deg, var(--navy) 0%, var(--navy-light) 55%, var(--navy) 100%); color: var(--white); }
  .front-brand { position: absolute; left: 135px; top: 145px; display: flex; align-items: center; gap: 14px; }
  .brand-square { width: 40px; height: 40px; background: var(--white); flex: none; }
  .front-brand .brand-name { font-size: 50px; line-height: 1; letter-spacing: 0.5px; white-space: nowrap; }
  .front-tagline { position: absolute; left: 189px; top: 216px; font-family: "Montserrat", sans-serif; font-weight: 600; font-size: 13px; letter-spacing: 0.5px; color: #9a9a9a; white-space: nowrap; }
  .front-url { position: absolute; left: 0; right: 0; top: 333px; text-align: center; font-size: 16px; letter-spacing: 0.3px; }

  /* Back */
  .card-back { top: 521px; background: var(--white); }
  .back-brand { position: absolute; left: 67px; top: 40px; display: flex; align-items: center; gap: 9px; color: var(--navy); }
  .back-brand .brand-square { width: 22px; height: 22px; background: var(--navy); }
  .back-brand .brand-name { font-size: 29px; line-height: 1; white-space: nowrap; }
  .back-tagline { position: absolute; left: 98px; top: 78px; font-family: "Montserrat", sans-serif; font-weight: 600; font-size: 8px; letter-spacing: 0.3px; color: var(--text-grey); white-space: nowrap; }

  .person { position: absolute; left: 82px; top: 186px; }
  .person-name { font-family: "Montserrat", sans-serif; font-weight: 700; font-size: 18px; color: var(--navy); letter-spacing: 0.5px; }
  .person-title { font-size: 15px; color: var(--text-grey); margin-top: 3px; }

  .contact-list { position: absolute; left: 82px; top: 246px; list-style: none; font-size: 15px; color: var(--text-grey); line-height: 19.5px; }
  .contact-list li { display: flex; align-items: center; gap: 5px; }
  .contact-list svg { width: 11px; height: 11px; fill: var(--navy); flex: none; }

  .company-info { position: absolute; right: 37px; top: 234px; text-align: right; font-size: 15px; color: var(--text-grey); line-height: 19px; }
  .company-info strong { font-family: "Montserrat", sans-serif; font-weight: 700; font-size: 14px; }
  .company-address { margin-top: 14px; }

  .footer-band-navy { position: absolute; left: 0; bottom: 0; width: 514px; height: 11px; background: var(--navy); }
  .footer-band-grey { position: absolute; right: 0; bottom: 0; width: 114px; height: 11px; background: var(--grey); }
</style>
</head>
<body>
  <section class="card card-front">
    <div class="front-brand"><span class="brand-square"></span><span class="brand-name">ironquill build</span></div>
    <div class="front-tagline">CONSTRUCTION • PROJECTS • RENOVATIONS • ADVICE</div>
    <div class="front-url">www.ironquillbuild.com.au</div>
  </section>

  <section class="card card-back">
    <div class="back-brand"><span class="brand-square"></span><span class="brand-name">ironquill build</span></div>
    <div class="back-tagline">CONSTRUCTION • PROJECTS • RENOVATIONS • ADVICE</div>

    <div class="person">
      <div class="person-name">DANIEL REEVE</div>
      <div class="person-title">Managing Director</div>
    </div>

    <ul class="contact-list">
      <li><svg viewBox="0 0 12 12"><path d="M3 0.5l2 2.5-1.2 1.3c.6 1.5 1.8 2.8 3.4 3.5L8.5 6.6 11 8.6 9.8 11C5 10.6 1.3 6.8 1 2z"/></svg>1300 587 902</li>
      <li><svg viewBox="0 0 12 12"><path d="M3 0h6a1 1 0 011 1v10a1 1 0 01-1 1H3a1 1 0 01-1-1V1a1 1 0 011-1zm0.8 1.5v7.5h4.4V1.5zM6 9.7a.7.7 0 100 1.4.7.7 0 000-1.4z"/></svg>0438 761 205</li>
      <li><svg viewBox="0 0 12 12"><path d="M0 2.5h12v7H0zm1 1v.3l5 3 5-3v-.3zm0 1.4V8.5h10V4.9l-5 3z"/></svg>name@ironquillbuild.com.au</li>
      <li><svg viewBox="0 0 12 12"><path d="M6 0a6 6 0 110 12A6 6 0 016 0zm-.6 1.2C4.2 2.5 3.7 4 3.6 5.5h1.8zm1.2 0v4.3h1.8C8.3 4 7.8 2.5 6.6 1.2zM1.1 5.5h1.5c.1-1.4.5-2.7 1.2-3.8A5 5 0 001.1 5.5zm7.2-3.8c.7 1.1 1.1 2.4 1.2 3.8h1.4a5 5 0 00-2.6-3.8zM1.1 6.5a5 5 0 002.7 3.8c-.7-1.1-1.1-2.4-1.2-3.8zm2.5 0c.1 1.5.6 3 1.8 4.3V6.5zm3 0v4.3c1.2-1.3 1.7-2.8 1.8-4.3zm2.8 0c-.1 1.4-.5 2.7-1.2 3.8a5 5 0 002.7-3.8z"/></svg>www.ironquillbuild.com.au</li>
    </ul>

    <div class="company-info">
      <div><strong>National Provider Number:</strong> 7192</div>
      <div><strong>ABN:</strong> 53 614 289 117</div>
      <div class="company-address">Level 1, 214 Garrow Street<br>Hexham NSW 2322</div>
    </div>

    <div class="footer-band-navy"></div>
    <div class="footer-band-grey"></div>
  </section>
</body>
</html>
```